BoltCrewBoard Postcard Campaign

We need a postcard design for our company, BoltCrewBoard.com - we are a job board for mechanics and auto technicians. We are sending a postcard to 1000 auto shops and trucking companies across the US to try to get them to come to our website and purchase a job pack and post a job posting. We will be offering them a promotion of "Save $20 on your first job post. Enter 'SUMMER20' at checkout."

We would like to see designs that are consistent with our website theme. The final design should communicate:
- Access to a targeted and local audience of only auto and truck mechanics and technicians
- Search 50,000 resumes
- Money back guarantee

Target Market(s)

Auto mechanic shops, car dealerships looking for mechanics, truck fleet management looking for technicians

Industry/Entity Type

It Company

Font styles to use
Sans Serif

Colors
0392cd
ec1f27
1b1b1b
cbcbcb
ffffff
3277b5

Requirements
Must have
• See content/copy upload
• - Match website color scheme and look and feel
Should not have
• No photos that look like stock photos - preferably steer away from photos unless it looks great

```html
<!DOCTYPE html>
<html lang="en">
<head>
<meta charset="utf-8">
<title>BoltCrewBoard Postcard – Front</title>
<link rel="stylesheet" href="https://fonts.googleapis.com/css2?family=Roboto+Condensed:ital,wght@0,400;0,700;1,400;1,700&display=swap">
<style>
  :root {
    --blue-deep: #1d4a78;
    --blue-mid: #3277b5;
    --blue-bright: #0392cd;
    --red: #ec1f27;
    --red-deep: #a61c20;
    --grey-light: #e4e5e7;
    --grey: #cbcbcb;
    --grey-dark: #8f9296;
    --ink: #1b1b1b;
    --white: #ffffff;
    --icon-cream: #f7e3da;
  }
  * { margin: 0; padding: 0; box-sizing: border-box; }
  html, body { width: 1200px; height: 1000px; overflow: hidden; background: var(--white); }
  body { position: relative; font-family: "Roboto Condensed", "Arial Narrow", sans-serif; }

  .postcard {
    position: absolute; left: 60px; top: 66px; width: 1073px; height: 832px;
    overflow: hidden;
    box-shadow: 4px 6px 10px rgba(0,0,0,0.45);
    background: var(--blue-deep);
  }
  .band-top {
    position: absolute; left: 0; top: 0; width: 100%; height: 316px;
    background: radial-gradient(ellipse at 60% 30%, var(--blue-mid) 0%, #2a5f95 45%, var(--blue-deep) 100%);
  }
  .band-middle {
    position: absolute; left: 0; top: 316px; width: 100%; height: 380px;
    background: radial-gradient(ellipse at 50% 35%, var(--grey-light) 0%, var(--grey) 45%, var(--grey-dark) 100%);
  }
  .band-bottom {
    position: absolute; left: 0; top: 696px; width: 100%; height: 136px;
    background: radial-gradient(ellipse at 50% 50%, var(--blue-mid) 0%, #2a5f95 50%, var(--blue-deep) 100%);
  }

  .headline { position: absolute; left: 0; top: 0; width: 100%; color: var(--white); font-weight: 400; text-shadow: 0 2px 8px rgba(0,0,0,0.3); }
  .headline span { position: absolute; font-size: 112px; line-height: 1; letter-spacing: 1px; white-space: nowrap; }
  .headline .line-one { left: 52px; top: 38px; }
  .headline .line-two { right: 56px; top: 152px; }

  .feature {
    position: absolute; top: 269px; width: 288px; height: 298px;
    background: radial-gradient(circle at 50% 40%, var(--red) 0%, #d0232a 45%, var(--red-deep) 100%);
    box-shadow: 0 3px 8px rgba(0,0,0,0.35);
    color: var(--white); text-align: center;
  }
  .feature--post { left: 85px; }
  .feature--reach { left: 391px; }
  .feature--search { left: 695px; }
  .feature svg { position: absolute; left: 50%; top: 28px; transform: translateX(-50%); }
  .feature p {
    position: absolute; left: 14px; right: 14px; font-size: 20px; line-height: 35px;
    text-shadow: 0 1px 4px rgba(0,0,0,0.35);
  }
  .feature--post p, .feature--reach p { top: 146px; }
  .feature--search p { top: 168px; }
  .feature em { font-style: italic; }

  .tagline {
    position: absolute; left: 0; top: 590px; width: 100%; text-align: center;
    color: var(--white); font-weight: 700; font-style: italic; font-size: 29px; line-height: 44px;
    text-shadow: 0 2px 5px rgba(0,0,0,0.45);
  }

  .contact {
    position: absolute; left: 0; top: 696px; width: 100%; height: 136px;
    display: flex; align-items: center; justify-content: center; gap: 26px;
    color: var(--white); font-weight: 700; text-shadow: 0 2px 5px rgba(0,0,0,0.4);
  }
  .contact .site { font-size: 40px; letter-spacing: 0.5px; }
  .contact .mark { width: 48px; height: 48px; border-radius: 50%; background: var(--white); }
  .contact .phone { font-size: 44px; letter-spacing: 1px; }

  .sheet-label {
    position: absolute; right: 67px; top: 938px; font-family: Arial, Helvetica, sans-serif;
    font-size: 20px; color: var(--ink);
  }
</style>
</head>
<body>
  <article class="postcard">
    <div class="band-top"></div>
    <div class="band-middle"></div>
    <div class="band-bottom"></div>

    <h1 class="headline">
      <span class="line-one">FIND YOUR NEXT</span>
      <span class="line-two">MECHANIC TODAY</span>
    </h1>

    <section class="feature feature--post">
      <svg width="104" height="104" viewBox="0 0 104 104" aria-hidden="true">
        <g fill="none" stroke="var(--icon-cream)" stroke-width="6" stroke-linejoin="round" stroke-linecap="round">
          <path d="M14 8 H62 L76 22 V94 H14 Z"/>
          <line x1="26" y1="34" x2="56" y2="34"/>
          <line x1="26" y1="48" x2="52" y2="48"/>
          <line x1="26" y1="62" x2="46" y2="62"/>
          <line x1="26" y1="76" x2="42" y2="76"/>
        </g>
        <path d="M86 20 L98 32 L62 70 L46 76 L52 60 Z" fill="var(--icon-cream)"/>
      </svg>
      <p>Post a job with us and get access to hundreds of qualified technicians in your area</p>
    </section>

    <section class="feature feature--reach">
      <svg width="140" height="104" viewBox="0 0 140 104" aria-hidden="true">
        <g fill="none" stroke="var(--icon-cream)" stroke-width="5" stroke-linejoin="round" stroke-linecap="round">
          <rect x="28" y="8" width="66" height="56" rx="3"/>
          <path d="M14 92 L26 68 H96 L108 92 Z"/>
          <path d="M104 22 Q110 30 104 38"/>
          <path d="M111 16 Q121 30 111 44"/>
          <path d="M118 10 Q132 30 118 50"/>
        </g>
        <g fill="var(--icon-cream)">
          <rect x="34" y="74" width="54" height="4"/>
          <rect x="30" y="81" width="62" height="4"/>
          <rect x="48" y="88" width="26" height="3"/>
        </g>
      </svg>
      <p>Includes distribution and promotion across multiple job boards, such as <em>HireLane.com</em>, <em>JobHarbor.com</em>, <em>WorkCrest.com</em></p>
    </section>

    <section class="feature feature--search">
      <svg width="120" height="110" viewBox="0 0 120 110" aria-hidden="true">
        <rect x="6" y="8" width="82" height="86" rx="12" fill="var(--icon-cream)"/>
        <rect x="6" y="8" width="82" height="16" rx="8" fill="#e8cbc0"/>
        <circle cx="66" cy="56" r="28" fill="var(--red)" stroke="var(--icon-cream)" stroke-width="3"/>
        <circle cx="66" cy="56" r="19" fill="var(--icon-cream)"/>
        <line x1="56" y1="52" x2="76" y2="52" stroke="var(--red)" stroke-width="4" stroke-linecap="round"/>
        <line x1="56" y1="60" x2="70" y2="60" stroke="var(--red)" stroke-width="4" stroke-linecap="round"/>
        <line x1="86" y1="76" x2="104" y2="94" stroke="var(--icon-cream)" stroke-width="12" stroke-linecap="round"/>
      </svg>
      <p>Search 50,000+ resumes, with new candidates added daily</p>
    </section>

    <p class="tagline">Connecting automotive employers with qualified technicians since 2006<br>100% satisfaction guaranteed, or your money back!</p>

    <footer class="contact">
      <span class="site">BOLTCREWBOARD.COM</span>
      <span class="mark" aria-hidden="true"></span>
      <span class="phone">800.555.0142</span>
    </footer>
  </article>

  <div class="sheet-label">FRONT POSTCARD</div>
</body>
</html>
```